Award-winnning Estate Agent needs a premium version of their 'For Sale' board design

We need a premium option for our 'For Sale' board design. We have a standard board that is attached to this brief, but were are looking to have a premium design version that we will use when selling exclusive properties. Our company name is Harbour Lane Estates and the name for this is exclusive selection is: 'The Harbour Collection'. The design needs to work with our current brand, but have a distinctive PREMIUM feel to it. I have uploaded the barnd guidelines and also some of the exisisting logo variations. We do NOT need a new logo but feel free to play around with colours, fonts, sizes etc. for the sign.

Target Market(s)

Property buyers & house hunters

Industry/Entity Type

Real Estate - Residential Property

Font styles to use
Sans Serif

Requirements
Must have
• A premium fee, must be square design, must be easy to read when driving past the sign
Nice to have
• I'm open ot ideas

```html
<!DOCTYPE html>
<html lang="en">
<head>
<meta charset="utf-8">
<title>Harbour Lane Estates – For Sale Board</title>
<link href="https://fonts.googleapis.com/css2?family=Bebas+Neue&family=Roboto:wght@400;700&display=swap" rel="stylesheet">
<style>
  :root {
    --navy: #2b3592;
    --deep-navy: #1f2a7a;
    --brand-blue: #1c78c4;
    --sky-blue: #29a9e1;
    --cyan: #2ee6f0;
    --white: #ffffff;
    --page: #ececf1;
  }
  * { margin: 0; padding: 0; box-sizing: border-box; }
  html, body { width: 1200px; height: 607px; overflow: hidden; }
  body {
    background: var(--page);
    display: flex; align-items: center; justify-content: center;
    font-family: "Roboto", Arial, sans-serif;
  }
  .board {
    position: relative;
    width: 560px; height: 572px;
    background: var(--white);
    overflow: hidden;
    box-shadow: 0 4px 18px rgba(20, 30, 90, 0.25);
  }
  .board > * { position: absolute; }

  .brand {
    left: 173px; right: 0; top: 40px;
    display: flex; flex-direction: column; align-items: center; gap: 40px;
  }
  .brand-dot {
    width: 44px; height: 44px; border-radius: 50%;
    background: var(--brand-blue);
  }
  .brand-name {
    font-weight: 700; font-size: 29px; color: var(--navy);
    white-space: nowrap; letter-spacing: 0.2px;
  }

  .band-navy { top: 192px; height: 39px; background: var(--navy); }
  .band-navy.left { left: 0; width: 73px; }
  .band-navy.right { left: 173px; right: 0; }

  .panel-blue {
    top: 241px; bottom: 0;
    background: linear-gradient(160deg, #2183cf 0%, var(--brand-blue) 60%, #176fb8 100%);
  }
  .panel-blue.left { left: 0; width: 73px; }
  .panel-blue.right { left: 173px; right: 0; }

  .feature-column {
    left: 82px; width: 83px; top: 0; bottom: 0;
    background: linear-gradient(180deg, #33b3ea 0%, var(--sky-blue) 100%);
  }

  .headline {
    left: 173px; right: 0; top: 244px;
    text-align: center;
    white-space: nowrap;
    font-family: "Bebas Neue", "Oswald", sans-serif;
    font-weight: 400;
    font-size: 112px; line-height: 1; color: var(--white);
    letter-spacing: 0;
    transform: scaleY(1.28);
    transform-origin: center top;
  }

  .collection-strip {
    left: 173px; right: 0; top: 391px; height: 50px;
    background: var(--white);
    display: flex; align-items: center; justify-content: center;
    font-size: 30px; color: var(--navy); white-space: nowrap;
  }
  .collection-strip strong { font-weight: 700; margin-right: 8px; }

  .phone {
    left: 173px; right: 0; top: 455px;
    display: flex; align-items: center; justify-content: center; gap: 10px;
    white-space: nowrap;
    font-family: "Bebas Neue", "Oswald", sans-serif;
    font-size: 62px; line-height: 1; color: var(--white);
    letter-spacing: 1px;
  }
  .phone-icon { width: 48px; height: 48px; flex: none; }

  .web-band {
    left: 168px; right: 0; top: 522px; height: 35px;
    background: var(--navy);
    display: flex; align-items: center; justify-content: center;
    font-size: 22px; color: var(--white); white-space: nowrap;
  }
</style>
</head>
<body>
  <main class="board">
    <div class="panel-blue left"></div>
    <div class="panel-blue right"></div>
    <div class="band-navy left"></div>
    <div class="band-navy right"></div>
    <div class="feature-column" role="img" aria-label="Tall brand tower graphic"></div>

    <header class="brand">
      <span class="brand-dot"></span>
      <span class="brand-name">Harbour Lane Estates</span>
    </header>

    <h1 class="headline">FOR SALE!</h1>

    <p class="collection-strip"><strong>The Harbour</strong> Collection</p>

    <p class="phone">
      <svg class="phone-icon" viewBox="0 0 48 48" aria-hidden="true">
        <circle cx="24" cy="24" r="24" fill="var(--cyan)"/>
        <path d="M16 12c2 0 3 4 4 6s-2 3-2 4c1 3 4 6 7 7 1 0 2-3 4-2s6 2 6 4-2 5-5 5C20 36 12 28 12 18c0-3 2-6 4-6z" fill="var(--brand-blue)"/>
        <path d="M27 14a8 8 0 0 1 7 7M27 9a13 13 0 0 1 12 12" fill="none" stroke="var(--brand-blue)" stroke-width="2.4" stroke-linecap="round"/>
      </svg>
      01632 960418
    </p>

    <p class="web-band">www.harbourlaneestates.co.uk</p>
  </main>
</body>
</html>
```